Instagram ad design required

For an IT system house, we need an ad design for a job recruiting campaign on Instagram. A great engaging advertisement is required that encourages potential applicants to click on the ad. The recruiting funnel already exists, only an Instagram ad image should be designed. Follow-up orders for further campaigns as well as Facebook and LinkedIn are possible.
The design of the IT system house Dolvira serves as a design inspiration: www.dolvira.com
The customer should be perceived as a great, modern employer. The target group are young IT technicians who want to work in a cool and modern company. For example, the topic could be IT Super Hero wanted with corresponding graphic content.
Target Market(s)
IT system technician
Industry/Entity Type
Informatik
Other font styles liked:
- PT Sans
Look and feel

```html
<!DOCTYPE html>
<html lang="de">
<head>
<meta charset="UTF-8">
<title>Dolvira – IT-Superheld gesucht</title>
<link rel="stylesheet" href="https://fonts.googleapis.com/css2?family=Poppins:wght@400;500;600;700;800&display=swap">
<style>
  :root {
    --green-deep: #279458;
    --green-mid: #3aa862;
    --green-soft: #a9e6a2;
    --green-pale: #c9f2bd;
    --neon: #55f000;
    --neon-dark: #1f7a3c;
    --white: #ffffff;
    --headline-light: #f0ffe8;
  }
  html, body {
    margin: 0;
    padding: 0;
    width: 1200px;
    height: 1200px;
    overflow: hidden;
    background: var(--green-deep);
  }
  .canvas {
    width: 1200px;
    height: 1200px;
    overflow: hidden;
    position: relative;
  }
  .artboard {
    position: absolute;
    top: 0;
    left: 0;
    width: 1080px;
    height: 1080px;
    transform: scale(1.11111);
    transform-origin: 0 0;
    font-family: "Poppins", sans-serif;
    color: var(--white);
    background:
      radial-gradient(circle at 15% 85%, var(--green-soft) 0%, rgba(169,230,162,0) 45%),
      linear-gradient(135deg, var(--green-mid) 0%, var(--green-deep) 55%, #2a9a5c 100%);
    overflow: hidden;
  }
  .backdrop {
    position: absolute;
    inset: 0;
  }
  .photo-hero {
    position: absolute;
    left: 20px;
    top: 238px;
    width: 440px;
    height: 842px;
    border-radius: 200px 200px 0 0;
    background: linear-gradient(180deg, rgba(60,60,60,0.55) 0%, rgba(40,40,40,0.6) 40%, rgba(170,170,170,0.55) 75%, rgba(50,70,110,0.6) 100%);
  }
  .site-url {
    position: absolute;
    left: 40px;
    top: 58px;
    font-size: 27px;
    font-weight: 500;
    letter-spacing: 0.3px;
  }
  .brand {
    position: absolute;
    right: 46px;
    top: 52px;
    font-size: 44px;
    font-weight: 800;
    letter-spacing: 0.5px;
    line-height: 1;
  }
  .headline-top {
    position: absolute;
    left: 510px;
    top: 205px;
    font-size: 56px;
    font-weight: 600;
    color: var(--headline-light);
    line-height: 1;
  }
  .headline-main {
    position: absolute;
    left: 386px;
    top: 232px;
    font-size: 166px;
    font-weight: 600;
    color: var(--neon);
    letter-spacing: -3px;
    line-height: 1;
  }
  .subline {
    position: absolute;
    left: 675px;
    top: 390px;
    font-size: 29px;
    font-weight: 700;
    line-height: 1.3;
  }
  .skills {
    position: absolute;
    left: 693px;
    top: 555px;
    margin: 0;
    padding: 0;
    list-style: none;
  }
  .skill {
    display: flex;
    align-items: center;
    height: 58px;
    margin-bottom: 19px;
    font-size: 22px;
    font-weight: 500;
  }
  .skill-mark {
    width: 58px;
    height: 58px;
    background: var(--neon);
    margin-right: 14px;
    flex: none;
  }
  .contact {
    position: absolute;
    left: 700px;
    top: 936px;
  }
  .contact-label {
    font-size: 20px;
    font-weight: 700;
    margin: 0;
  }
  .contact-mail {
    font-size: 20px;
    font-weight: 400;
    margin: 4px 0 0;
  }
  .cta {
    position: absolute;
    left: 700px;
    top: 1000px;
    font-size: 40px;
    font-weight: 700;
    margin: 0;
  }
</style>
</head>
<body>
<div class="canvas">
  <div class="artboard">
    <svg class="backdrop" width="1080" height="1080" viewBox="0 0 1080 1080" aria-hidden="true">
      <circle cx="215" cy="30" r="340" fill="none" stroke="rgba(255,255,255,0.16)" stroke-width="120"/>
      <circle cx="215" cy="30" r="200" fill="none" stroke="rgba(255,255,255,0.22)" stroke-width="60"/>
      <circle cx="300" cy="760" r="360" fill="var(--green-soft)" opacity="0.75"/>
    </svg>

    <div class="photo-hero" role="img" aria-label="Lächelnder junger IT-Techniker im dunklen Hemd, der ein geöffnetes PC-Gehäuse trägt"></div>

    <div class="site-url">www.dolvira.com</div>
    <div class="brand">DOLVIRA</div>

    <h1 style="margin:0">
      <span class="headline-top">IT-Superheld</span>
      <span class="headline-main">Gesucht</span>
    </h1>
    <p class="subline" style="margin:0">Werden Sie Teil unseres<br>großartigen Teams</p>

    <ul class="skills">
      <li class="skill">
        <svg class="skill-mark" viewBox="0 0 58 58" aria-hidden="true"><rect width="58" height="58" fill="var(--neon)"/><path d="M29 20v18M20 29h18" stroke="var(--neon-dark)" stroke-width="4"/></svg>
        Computerfähigkeiten
      </li>
      <li class="skill">
        <svg class="skill-mark" viewBox="0 0 58 58" aria-hidden="true"><rect width="58" height="58" fill="var(--neon)"/><path d="M29 20v18M20 29h18" stroke="var(--neon-dark)" stroke-width="4"/></svg>
        Computer Reparaturen
      </li>
      <li class="skill">
        <svg class="skill-mark" viewBox="0 0 58 58" aria-hidden="true"><rect width="58" height="58" fill="var(--neon)"/><path d="M29 20v18M20 29h18" stroke="var(--neon-dark)" stroke-width="4"/></svg>
        Technischer Support
      </li>
    </ul>

    <div class="contact">
      <p class="contact-label">Lebenslauf Senden An:</p>
      <p class="contact-mail">deine E-Mail@dolvira.com</p>
    </div>
    <p class="cta">Jetzt bewerben!</p>
  </div>
</div>
</body>
</html>
```